Self-Help & Training Association Business Card Design Project

We need double-sided business card for our Self-Help and Training Association called "Crescitalba".

We want Pibo.com to print them, both Velta and Standard Business Card format (**PLEASE DON'T SUBMIT ROUNDED-CORNERS CARDS).

(more info: http://uk.pibo-print.example)

We ask designers to submit project based on our logo (attached) and color-set and to do it according to Pibo.com designing guidelines.

We will print three variations (for three people) of the business card.

Let's apply now!

Thank you!

Target Market(s)

Common people

Industry/Entity Type

Business

Requirements
Must have
• Strings needed:

Association Name: Crescitalba
Tagline: Formarsi per Vivere Meglio
Web: www.crescitalba.example

Person Name: Luca Ferrandi
Person Title: Direttore Scientifico e Lead Trainer
Mobile: (+39) 347 5081934
E-mail: luca@crescitalba.example

Could be a nice idea to put general details on the front and personal details on the back of the card.

-
Artwork guidelines
You can use PIBO's online tools to position and crop your images, but if you'd like to pre-design your Business Cards, before you upload these are the dimensions you need:

Full bleed size
(Recommended for creating artwork - this includes the bleed, which will be cropped in production. Please note, you do not need to add crop marks to your artwork)

1039 x 697 pixels (300dpi)
88mm x 59mm (300dpi)
3.46" x 2.32" (300dpi)
Final size when trimmed
84mm x 55mm
3.30" x 2.16"
Accepted file types
We accept high resolution GIFs, PNGs, PDFs, and JPGs.

-

See http://www.crescitalba.example/ for colors and style reference.

Thank you!
Nice to have
• If you still have empty space, this quote will be cool to be added:

"Non è il più forte o il più intelligente a sopravvivere, ma chi si adatta più velocemente al cambiamento. (G. Pellow)"

```html
<!DOCTYPE html>
<html lang="it">
<head>
<meta charset="utf-8">
<title>Crescitalba – Biglietto da visita, retro</title>
<link rel="stylesheet" href="https://fonts.googleapis.com/css2?family=Libre+Baskerville:wght@700&display=swap">
<style>
  :root {
    --band-top: #3d3d3d;
    --band-top-light: #555555;
    --centre-grey: #6e6e6e;
    --centre-light: #737373;
    --centre-blue: #5d6a75;
    --bottom-blue: #4f5563;
    --bottom-dark: #363640;
    --rule: #0a0a0a;
    --ink: #343434;
  }
  * { margin: 0; padding: 0; box-sizing: border-box; }
  html, body { width: 1200px; height: 686px; overflow: hidden; background: #ffffff; }
  .card {
    position: relative;
    width: 1200px;
    height: 686px;
    overflow: hidden;
    background: linear-gradient(to bottom, var(--band-top) 0%, var(--band-top-light) 25%);
  }
  .band-top {
    position: absolute; left: 0; top: 0; width: 100%; height: 171px;
    background: linear-gradient(to bottom, #3b3b3b 0%, #474747 50%, #5a5a5a 100%);
  }
  .band-centre {
    position: absolute; left: 0; top: 171px; width: 100%; height: 298px;
    background: linear-gradient(to bottom, #686868 0%, var(--centre-light) 40%, var(--centre-blue) 62%, #565c66 100%);
  }
  .band-bottom {
    position: absolute; left: 0; top: 469px; width: 100%; height: 217px;
    background: linear-gradient(to bottom, var(--bottom-blue) 0%, #454854 45%, var(--bottom-dark) 100%);
  }
  .rule {
    position: absolute; left: 0; width: 100%; height: 6px; background: var(--rule);
  }
  .rule-top { top: 168px; }
  .rule-bottom { top: 466px; }
  .contact {
    position: absolute; left: 0; top: 205px; width: 100%;
    text-align: center;
    font-family: "Libre Baskerville", "Palatino Linotype", Georgia, serif;
    font-weight: 700;
    font-size: 38px;
    line-height: 57px;
    color: var(--ink);
    letter-spacing: -0.3px;
  }
  .contact p { white-space: nowrap; }
</style>
</head>
<body>
  <main class="card">
    <div class="band-top"></div>
    <div class="band-centre"></div>
    <div class="band-bottom"></div>
    <div class="rule rule-top"></div>
    <div class="rule rule-bottom"></div>
    <section class="contact">
      <p class="contact-name">Luca Ferrandi</p>
      <p class="contact-title">Direttore Scientifico e Lead Trainer</p>
      <p class="contact-phone">(+39) 347 5081934</p>
      <p class="contact-email">luca@crescitalba.example</p>
    </section>
  </main>
</body>
</html>
```